Hollow Lantern Double Sided Flyer Design

We need a double sided flyer (1/3 of an A4 which is 99mm x 210mm) developed for our Newcastle(NSW) tour. This flyer will be placed in tourist information centres and hotels. We want it to direct people to our website or be able to make bookings over the phone.

About Us:-
We are a city walking tour company that runs tours day or night. We run both day and night and will incorporate real history / real Hollow lantern. Some of the stories will be quite serious i.e.- there are infamous murders from 100 years ago, baffling court cases, even a bit of poetry written by murderers, suicides, love triangles, you name it. We will be telling the historical stories that tourists will not hear from any other tour provider. A bit of darkness, a bit of mystery and a bit of history theme.

We do no go for scares and let the very real stories deliver the entertainment for our guests. Our customers enjoy our tours, but it isn't light fun and frivolity. Our stories are being carefully crafted and are packed with unexpected twists, turns; revelations whilst remaining all 100% true. We deliver deep, rich, engaging stories.

Here are a few samples of quotes from the characters in our stories that may give you an idea of the kind of history we will cover:-

"There were bits of spines, bits of skulls, [and] finger bones spilled out all over the streets - I ended up filling three boxes. Children were playing with them for weeks”

"I had a close shave last night and now I want a close haircut.”

“She's a beautiful child', isn't she? She's the cause of all the trouble.”

“I did it because she would not come home with me.”

"I have killed my wife. I’m glad she’s dead.”

"Stand aside or I'll put a bullet through both of you."

“You villain, I'll teach you to take away my character."

“You’re not dead yet, you bastard!”

Our website, booking form and contact details can be viewed at www.hollowlantern-tours.com.au

Target Market(s)

Tourists

Industry/Entity Type

Tour

Colors

Designer to choose colors to be used in the design.

Requirements
Must have
• Vertical orientation please.
• Please also include a reference to a discount offer of 25% using the promo code "DARK".
Nice to have
• FRONT FLYER INFORMATION
• - Hollow Lantern Logo
• - "I have killed my wife; I'm glad she's dead."
• - Harbourside Buried Past Walk
• - 25% Discount Offer Codeword DARK
• - web address at the base; www.hollowlantern-tours.com.au
• BACK FLYER INFORMATION
• - "She's a beautiful child', isn't she? She's the cause of all the trouble.
• - Hollow Lantern Logo at the base along with the web address www.hollowlantern-tours.com.au
• - Blurb:- Hollow lantern brings back Newcastle's hidden past, the forgotten past, the dark past that may not want to be remembered.
• Real stories from the streets around you. Discover the histories you won't hear anywhere else. The forgotten stories of yesteryear finally get a chance to be told. Through you they get to live again.
Should not have
• GENERAL
• Please do not include the phone number, email address or social media icons. We want to drive online bookings.

```html
<!DOCTYPE html>
<html lang="en">
<head>
<meta charset="utf-8">
<title>Hollow Lantern – Double Sided Flyer</title>
<link href="https://fonts.googleapis.com/css2?family=Lato:wght@400;700&display=swap" rel="stylesheet">
<style>
  :root {
    --backdrop: #a7a8ab;
    --brand-red: #e3262b;
    --ink: #333435;
    --body-ink: #3a3a3a;
    --paper: #ffffff;
    --pill-dark: #303133;
  }
  * { box-sizing: border-box; margin: 0; padding: 0; }
  html, body { width: 1200px; height: 1193px; overflow: hidden; }
  body {
    background: var(--backdrop);
    font-family: "Lato", sans-serif;
    position: relative;
  }
  .flyer {
    position: absolute;
    top: 84px;
    width: 479px;
    height: 1016px;
    background: var(--paper);
    overflow: hidden;
    box-shadow: 6px 8px 14px rgba(0,0,0,0.35);
  }
  .flyer--front { left: 93px; }
  .flyer--back { left: 622px; }

  .hero-photo { position: absolute; left: 0; top: 0; width: 100%; }
  .flyer--front .hero-photo {
    height: 640px;
    background: linear-gradient(180deg, #1c2230 0%, #3a4150 22%, #6b6450 38%, #a98f55 46%, #5d5a44 55%, #6f6a5c 66%, #3f4048 82%, #2a2c33 100%);
  }
  .flyer--back .hero-photo {
    height: 500px;
    background: linear-gradient(180deg, #1b1b1b 0%, #3a3a3a 20%, #2b2b2b 45%, #454545 70%, #262626 100%);
  }
  .curve { position: absolute; left: 0; top: 0; width: 100%; }

  .brand-name {
    position: absolute; left: 0; width: 100%;
    text-align: center; font-weight: 700; letter-spacing: 0.5px;
  }
  .flyer--front .brand-name { top: 134px; font-size: 30px; color: var(--paper); }
  .flyer--back .brand-name { top: 902px; font-size: 30px; color: var(--ink); }

  .tour-title {
    position: absolute; top: 204px; left: 0; width: 100%;
    text-align: center; color: var(--paper); font-size: 16px; text-transform: uppercase;
  }
  .pull-quote {
    position: absolute; color: var(--paper); font-weight: 700;
    text-shadow: 0 2px 5px rgba(0,0,0,0.6);
  }
  .flyer--front .pull-quote { left: 62px; top: 412px; font-size: 28px; line-height: 31px; }
  .flyer--front .pull-quote span { display: block; padding-left: 95px; }
  .flyer--back .pull-quote {
    left: 0; width: 100%; top: 162px; text-align: center; font-size: 29px; line-height: 36px;
  }

  .body-copy {
    position: absolute; left: 50%; transform: translateX(-50%);
    text-align: center; color: var(--body-ink);
  }
  .flyer--front .body-copy { top: 610px; width: 360px; font-size: 16px; line-height: 20.5px; }
  .flyer--back .body-copy { top: 508px; width: 362px; font-size: 20px; line-height: 24.6px; }
  .flyer--back .body-copy p + p { margin-top: 24px; }

  .section-title {
    position: absolute; top: 448px; left: 0; width: 100%;
    text-align: center; color: var(--brand-red); font-size: 29px; font-weight: 700;
  }

  .offer { position: absolute; left: 74px; top: 800px; display: flex; align-items: center; }
  .offer__percent { color: var(--brand-red); font-size: 74px; font-weight: 700; line-height: 1; letter-spacing: -1px; }
  .offer__label { margin-left: 18px; color: var(--ink); font-size: 34px; line-height: 30px; text-transform: uppercase; }

  .codeword {
    position: absolute; left: 75px; top: 886px; width: 329px; height: 47px;
    display: flex; border-radius: 24px; overflow: hidden; font-size: 25px;
  }
  .codeword__label {
    width: 168px; background: var(--pill-dark); color: var(--paper);
    display: flex; align-items: center; justify-content: center;
  }
  .codeword__value {
    flex: 1; background: var(--brand-red); color: var(--paper); font-size: 32px;
    display: flex; align-items: center; justify-content: center; border-radius: 24px 0 0 24px;
  }

  .site-band {
    position: absolute; left: 0; bottom: 0; width: 100%; height: 51px;
    background: var(--brand-red); color: var(--paper);
    display: flex; align-items: center; justify-content: center; font-size: 25px;
  }
</style>
</head>
<body>

  <section class="flyer flyer--front">
    <div class="hero-photo" role="img" aria-label="Photo of a city skyline at sunset reflected in a calm river"></div>
    <svg class="curve" width="479" height="1016" viewBox="0 0 479 1016">
      <path d="M0 626 Q239.5 440 479 626 L479 1016 L0 1016 Z" fill="#ffffff"/>
      <path d="M0 612 Q239.5 424 479 612" fill="none" stroke="#e3262b" stroke-width="3"/>
    </svg>
    <div class="brand-name">HOLLOW LANTERN</div>
    <div class="tour-title">Harbourside Buried Past Walk</div>
    <div class="pull-quote">"I have killed my wife;<span>I'm glad she's dead."</span></div>
    <div class="body-copy">Dark; a euphemism for the unknown or the forgotten.....the dark ages, dark matter, dark energy; things where knowledge is uncertain or unknown are dark.&nbsp; Hollow lantern brings back the hidden past, the forgotten past, the past that may not want to be remembered......but these are real stories....real stories that come from the streets around you.</div>
    <div class="offer">
      <div class="offer__percent">25%</div>
      <div class="offer__label">Discount<br>Offer</div>
    </div>
    <div class="codeword">
      <div class="codeword__label">Codeword</div>
      <div class="codeword__value">DARK</div>
    </div>
    <div class="site-band">www.hollowlantern-tours.com.au</div>
  </section>

  <section class="flyer flyer--back">
    <div class="hero-photo" role="img" aria-label="Black and white aerial photo of a coastal city with streets and buildings"></div>
    <svg class="curve" width="479" height="1016" viewBox="0 0 479 1016">
      <path d="M0 490 Q239.5 302 479 490 L479 1016 L0 1016 Z" fill="#ffffff"/>
      <path d="M0 481 Q239.5 286 479 481" fill="none" stroke="#e3262b" stroke-width="3"/>
    </svg>
    <div class="pull-quote">She's a beautiful child',<br>isn't she? She's the cause of<br>all the trouble.</div>
    <div class="section-title">About Us</div>
    <div class="body-copy">
      <p>Hollow lantern brings back Newcastle's hidden past, the forgotten past, the dark past that may not want to be remem-<br>bered.</p>
      <p>- Real stories from the streets around you. Discover the histories you won't hear anywhere else. The forgotten stories of yesteryear finally get a chance to be told. Through you they get to live again.</p>
    </div>
    <div class="brand-name">HOLLOW LANTERN</div>
    <div class="site-band">www.hollowlantern-tours.com.au</div>
  </section>

</body>
</html>
```